Unique Extrior cleaning Logo

We need a new business card design, i would like to use our existing logo (attached).
Our logo on the left & a unique graphic design on the right of either a man holding a pressure washer gun & hose with a thumbs up or an image portraying dirt melting off a building or the two incorperated together, or something similar that represents exterior cleaning in progress, an image that shows/explains that we are exterior cleaners/pressure washers. Has to incorporate the google & facebook symbol perhaps in the bottom corners of the business card.
Existing business symbol on the back of the card with some blank lines for space to hand write quotes or job notes.
Industry/Entity Type
Exterior Cleaning
Contact Information for Business Card
Business mobile No. to be prominent (0487 214 960) Services provided listed as dot points. -Soft Washing -Pressure Washing - Solar Panel Cleaning - All General Exterior Cleaning. Email listed in fineprint (enquiries@brightvalewashcrew.com.au). Owner Operator - Desmond Fairlie (this should also be added somewhere prominent). Residential & Comercial Cleaning.
Colors
Designer to choose colors to be used in the design.
Look and feel

```html
<!DOCTYPE html>
<html lang="en">
<head>
<meta charset="utf-8">
<title>Brightvale Wash Crew – Business Card</title>
<link rel="stylesheet" href="https://fonts.googleapis.com/css2?family=Lato:wght@400;700;900&display=swap">
<style>
  :root {
    --brand-blue: #3462e0;
    --ink: #111111;
    --paper: #ffffff;
    --stage: #2e2e2e;
    --muted: #333333;
  }
  * { margin: 0; padding: 0; box-sizing: border-box; }
  html, body { width: 1200px; height: 875px; overflow: hidden; }
  body {
    background: var(--stage);
    font-family: "Lato", Arial, sans-serif;
    position: relative;
  }
  .card {
    position: absolute;
    width: 600px;
    height: 343px;
    background: var(--paper);
    border-radius: 16px;
    overflow: hidden;
    box-shadow: 0 18px 40px rgba(0,0,0,.45);
  }
  .card--back { left: 300px; top: 52px; }
  .card--front { left: 300px; top: 480px; }

  /* Back */
  .back-band {
    position: absolute; left: 0; top: 0; width: 150px; height: 100%;
    background: var(--brand-blue);
  }
  .services {
    position: absolute; right: 40px; top: 120px;
    list-style: none; text-align: right;
  }
  .services li {
    font-size: 15px; letter-spacing: 1px; text-transform: uppercase;
    color: var(--muted); line-height: 26px;
    display: flex; justify-content: flex-end; align-items: center; gap: 8px;
  }
  .tick { width: 14px; height: 14px; flex: none; }

  /* Front */
  .owner {
    position: absolute; right: 36px; top: 26px; text-align: right;
  }
  .owner__name {
    font-weight: 900; font-size: 24px; color: var(--ink); letter-spacing: .5px;
    text-transform: uppercase;
  }
  .owner__role { font-size: 15px; color: var(--brand-blue); letter-spacing: .5px; }
  .illustration {
    position: absolute; left: 350px; top: 92px; width: 215px; height: 150px;
    background: linear-gradient(135deg, #3462e0 0%, #6b8df0 100%);
    border-radius: 6px;
  }
  .brand {
    position: absolute; left: 40px; top: 78px;
    display: flex; align-items: center; gap: 12px;
  }
  .brand__mark { width: 26px; height: 26px; background: var(--brand-blue); flex: none; }
  .brand__name {
    font-weight: 900; font-size: 26px; line-height: 28px; color: var(--ink);
    text-transform: uppercase;
  }
  .contact { position: absolute; left: 40px; top: 172px; }
  .contact__row { display: flex; align-items: center; gap: 8px; color: var(--muted); }
  .contact__row--phone { font-size: 30px; font-weight: 700; color: var(--ink); margin-bottom: 4px; }
  .contact__row--fine { font-size: 12px; line-height: 18px; }
  .icon { width: 14px; height: 14px; flex: none; fill: var(--brand-blue); }
  .footer-shapes { position: absolute; left: 0; top: 0; width: 600px; height: 343px; }
  .social { position: absolute; left: 36px; bottom: 12px; display: flex; gap: 8px; }
  .social__dot { width: 22px; height: 22px; border-radius: 50%; background: var(--paper); }
  .tagline {
    position: absolute; right: 28px; bottom: 18px;
    color: var(--paper); font-weight: 700; font-size: 16px; letter-spacing: .3px;
  }
</style>
</head>
<body>

<section class="card card--back" aria-label="Card back">
  <div class="back-band"></div>
  <ul class="services">
    <li>Soft Washing <svg class="tick" viewBox="0 0 14 14"><circle cx="7" cy="7" r="7" fill="#3462e0"/><path d="M4 7.2l2 2 4-4.2" stroke="#fff" stroke-width="1.6" fill="none"/></svg></li>
    <li>Pressure Washing <svg class="tick" viewBox="0 0 14 14"><circle cx="7" cy="7" r="7" fill="#3462e0"/><path d="M4 7.2l2 2 4-4.2" stroke="#fff" stroke-width="1.6" fill="none"/></svg></li>
    <li>Solar Panel Cleaning <svg class="tick" viewBox="0 0 14 14"><circle cx="7" cy="7" r="7" fill="#3462e0"/><path d="M4 7.2l2 2 4-4.2" stroke="#fff" stroke-width="1.6" fill="none"/></svg></li>
    <li>All General Exterior Cleaning <svg class="tick" viewBox="0 0 14 14"><circle cx="7" cy="7" r="7" fill="#3462e0"/><path d="M4 7.2l2 2 4-4.2" stroke="#fff" stroke-width="1.6" fill="none"/></svg></li>
  </ul>
</section>

<section class="card card--front" aria-label="Card front">
  <svg class="footer-shapes" viewBox="0 0 600 343">
    <polygon points="0,343 0,300 300,262 288,343" fill="#3462e0"/>
    <polygon points="306,254 600,214 600,343 294,343" fill="#111111"/>
    <polygon points="300,262 306,254 294,343 288,343" fill="#ffffff"/>
  </svg>

  <div class="owner">
    <div class="owner__name">Desmond Fairlie</div>
    <div class="owner__role">Owner Operator</div>
  </div>

  <div class="illustration" role="img" aria-label="Silhouette of a worker using a pressure washer gun and hose beside a wheeled pressure-washer unit"></div>

  <div class="brand">
    <span class="brand__mark"></span>
    <span class="brand__name">Brightvale<br>Wash Crew</span>
  </div>

  <div class="contact">
    <div class="contact__row contact__row--phone">
      <svg class="icon" viewBox="0 0 24 24"><path d="M6.6 10.8a15.1 15.1 0 0 0 6.6 6.6l2.2-2.2c.3-.3.7-.4 1-.2 1.1.4 2.3.6 3.6.6.6 0 1 .4 1 1V20c0 .6-.4 1-1 1A17 17 0 0 1 3 4c0-.6.4-1 1-1h3.5c.6 0 1 .4 1 1 0 1.3.2 2.5.6 3.6.1.3 0 .7-.2 1z"/></svg>
      0487 214 960
    </div>
    <div class="contact__row contact__row--fine">
      <svg class="icon" viewBox="0 0 24 24"><path d="M2 5h20v14H2z M2 5l10 8 10-8" fill="#3462e0" stroke="#fff" stroke-width="1.5"/></svg>
      enquiries@brightvalewashcrew.com.au
    </div>
    <div class="contact__row contact__row--fine">
      <svg class="icon" viewBox="0 0 24 24"><circle cx="12" cy="12" r="10"/><path d="M2 12h20M12 2c3 3 3 17 0 20M12 2c-3 3-3 17 0 20" stroke="#fff" stroke-width="1.4" fill="none"/></svg>
      brightvalewashcrew.com.au
    </div>
  </div>

  <div class="social">
    <span class="social__dot"></span>
    <span class="social__dot"></span>
  </div>

  <div class="tagline">Residential &amp; Comercial Cleaning.</div>
</section>

</body>
</html>
```